Grafik für Homepage zur Entwicklung von Softwarelösungen
Zielgruppe
Wir entwickeln Softwarelösungen zur Digitalisierung des Maschinen und Anlagenbaus (Industrie 4.0). Unsere Zielgruppe sind Betreiber von Produktionsfabriken und Maschinen- und Anlagenbauer für die industrielle Produktion.
Aufgabenstellung
Die Graphik kommt auf die Home-Seite unserer Website. Sie soll zum Weiterlesen anregen, Interesse wecken, seriös aber gleichzeitig modern und fortschrittlich sein.
Sie soll deutlich machen, das wir auf die Maschinen / Equipment unserer Kunden eine IoT-Architektur aufbauen, die die Maschinen intelligent macht und neue, digitale Anwendungen und Geschäftsmodelle ermöglicht. Das ist auch in der bestehenden Graphik enthalten, die jedoch nicht attraktiv und ggf. zu technisch ist.
Der aktuelle Dummy der Webseite ist erreichbar unter: http://r-583.henrik-wamsler.de/
Die neue Graphik soll die bestehende auf der Home Seite ersetzen.
Einige Beispiele sind angehängt, die jedoch inhaltlich nicht passen. Es sind 2D und 3D Vorschläge willkommen.
NEUE BILDER bitte beachten!

```html
<!DOCTYPE html>
<html lang="de">
<head>
<meta charset="utf-8">
<title>Vernatec Systems – Digitalisierungslösungen</title>
<link rel="stylesheet" href="https://fonts.googleapis.com/css2?family=Alegreya+Sans:wght@700&family=Open+Sans:wght@400;600&family=Arimo:wght@700&display=swap">
<style>
  :root {
    --nav-bg: #ffffff;
    --hero-bg: #0f3e50;
    --nav-text: #555a5e;
    --nav-active: #8fb8c4;
    --logo-text: #3c4a52;
    --logo-ring: #8fa4ad;
    --headline: #ffffff;
    --body-text: #ffffff;
    --label-text: #c7d3da;
    --label-rule: #9fc2cd;
    --btn-primary-bg: #ffffff;
    --btn-primary-text: #2b3338;
    --art-a: #c8cdf5;
    --art-b: #3f8fd6;
    --art-c: #f1b94c;
  }
  * { box-sizing: border-box; margin: 0; padding: 0; }
  html, body { width: 1200px; height: 545px; overflow: hidden; }
  body { font-family: "Open Sans", Arial, sans-serif; background: var(--hero-bg); position: relative; }

  .site-header {
    position: absolute; left: 0; top: 0; width: 1200px; height: 86px;
    background: var(--nav-bg);
  }
  .brand {
    position: absolute; left: 58px; top: 30px;
    display: flex; align-items: center; gap: 8px;
    font-family: "Open Sans", Arial, sans-serif; font-weight: 600;
    font-size: 21px; color: var(--logo-text); letter-spacing: 0.3px;
  }
  .brand-dot {
    width: 24px; height: 24px; border-radius: 50%;
    border: 2px solid var(--logo-ring);
  }
  .main-nav {
    position: absolute; top: 35px; left: 532px;
    display: flex; gap: 27px; font-size: 13.3px; color: var(--nav-text);
  }
  .main-nav a { color: inherit; text-decoration: none; position: relative; }
  .main-nav a.is-active { color: var(--nav-active); }
  .main-nav a.is-active::after {
    content: ""; position: absolute; left: 0; right: 0; top: 49px;
    height: 2px; background: var(--nav-active);
  }

  .hero-copy { position: absolute; left: 53px; top: 183px; width: 490px; }
  .hero-title {
    font-family: "Alegreya Sans", "Open Sans", sans-serif; font-weight: 700;
    font-size: 25px; line-height: 33px; color: var(--headline);
  }
  .hero-lead {
    margin-top: 7px; font-size: 14.2px; line-height: 20px; color: var(--body-text);
  }
  .hero-actions { position: absolute; left: 53px; top: 383px; display: flex; gap: 17px; }
  .btn {
    height: 43px; display: flex; align-items: center; justify-content: center;
    font-size: 13.3px; border-radius: 3px; text-decoration: none;
  }
  .btn-primary { width: 228px; background: var(--btn-primary-bg); color: var(--btn-primary-text); }
  .btn-outline { width: 122px; border: 2px solid #ffffff; color: #ffffff; }

  .layer-list { position: absolute; left: 546px; top: 0; list-style: none; }
  .layer {
    position: absolute; left: 0; width: 160px;
    font-family: "Arimo", Arial, sans-serif; font-weight: 700;
    font-size: 15.5px; line-height: 21px; color: var(--label-text);
  }
  .layer::after {
    content: ""; display: block; width: 58px; height: 2px;
    margin-top: 4px; background: var(--label-rule);
  }
  .layer-business { top: 149px; }
  .layer-value { top: 221px; }
  .layer-twin { top: 294px; }
  .layer-connect { top: 364px; }
  .layer-equipment { top: 412px; }

  .factory-art {
    position: absolute; left: 685px; top: 129px; width: 476px; height: 356px;
    border-radius: 18px;
    background:
      radial-gradient(ellipse at 30% 55%, rgba(241,185,76,0.35), transparent 55%),
      linear-gradient(135deg, var(--art-a) 0%, var(--art-b) 55%, #2a5f8a 100%);
    opacity: 0.85;
  }
</style>
</head>
<body>
  <header class="site-header">
    <div class="brand"><span class="brand-dot"></span>Vernatec Systems</div>
    <nav class="main-nav">
      <a class="is-active" href="#">Home</a>
      <a href="#">Beratung</a>
      <a href="#">Softwareprodukte</a>
      <a href="#">Softwareentwicklung</a>
      <a href="#">Über uns</a>
      <a href="#">Kontakt</a>
    </nav>
  </header>

  <section class="hero-copy">
    <h1 class="hero-title">Ihre Maschinen + unsere<br>Digitalisierungslösungen =<br>bis zu 45 % mehr Produktivität</h1>
    <p class="hero-lead">Vernatec Systems ist Ihr kompetenter Partner für die digitale Transformation. Von der Maschine bis zum Geschäftsmodell sorgen wir für mehr digitale Wertschöpfung.</p>
  </section>

  <div class="hero-actions">
    <a class="btn btn-primary" href="#">Kostenfreie Erstberatung sichern</a>
    <a class="btn btn-outline" href="#">mehr erfahren</a>
  </div>

  <ul class="layer-list">
    <li class="layer layer-business">Digital<br>Business Model</li>
    <li class="layer layer-value">Digital<br>Added Value</li>
    <li class="layer layer-twin">IIOT<br>Digital Twin</li>
    <li class="layer layer-connect">Connectivity</li>
    <li class="layer layer-equipment">Equipment</li>
  </ul>

  <div class="factory-art" role="img" aria-label="Isometrische Illustration einer vernetzten Fabrik mit Förderbändern, Maschinen, Robotern, Dashboards und Tablet"></div>
</body>
</html>
```